Lawn Maintenance Company needs attractive add for local newspaper

My company Halvern Lawn Works offers many lawn and yard services but I want this add to focus on one specific service we offer.
- Lawn Fertilizer and Weed Control -

This will be an add for our local newspaper, likely a 1/4 page

Some more information about this service.
Our customers generally call us when their lawn is over run with weeds or is performing poorly. Most of the time we set them up with a program and we return to their property every 4 - 5 weeks for another application. 95% of our customers return the following year for the same program. If the customer wishes we will also do a one time application

email: halvernlawnworks@mailpost.test
phone: call or text 555-814-2937

Target Market(s)

- Local small towns, populations less than 20,000
- Residential and Commercial customers with lawns
- People who are using the competitors service and aren't happy with it

Industry/Entity Type

Lawn Care

Requirements
Must have
• Must include our logo, email address and phone number
• - Logo
• - Email address and phone number (call or text)
• - Must focus on the service we want to sell (fertilizer and weed control)
Nice to have
• Some phrases or words that should be included, does not need to be word for word as long as the point is made
• - We service both Residential & Commercial properties
• - We offer professional service that can dramatically improve your lawn whether you are looking for a single application or a season long fertilizer/weed control program
• - Our lawn techs are licensed and certified applicators
Should not have
• I do not want any stock pictures of people, houses or equipment.

```html
<!DOCTYPE html>
<html lang="en">
<head>
<meta charset="utf-8">
<title>Halvern Lawn Works – Fertilizer &amp; Weed Control</title>
<link rel="stylesheet" href="https://fonts.googleapis.com/css2?family=Noto+Serif:ital,wght@0,400;0,700;1,400&display=swap">
<style>
  :root {
    --sky-top: #8fc3ea;
    --sky-bottom: #eaf4fc;
    --brand-green: #0b5a2c;
    --pill-orange: #d9541e;
    --badge-blue: #2a4797;
    --bar-orange: #ef7f1a;
    --bar-orange-deep: #dc5522;
    --lawn-light: #7ccf3e;
    --lawn-mid: #4f9e2c;
    --lawn-dark: #2a5e1e;
    --ink: #1d1d1d;
    --white: #ffffff;
  }
  * { margin: 0; padding: 0; box-sizing: border-box; }
  html, body { width: 980px; height: 1200px; overflow: hidden; background: var(--white); }
  .ad {
    position: relative;
    width: 980px;
    height: 1200px;
    overflow: hidden;
    font-family: "Noto Serif", Georgia, serif;
    background: var(--white);
  }
  .sky {
    position: absolute; left: 0; top: 0; width: 980px; height: 415px;
    background: linear-gradient(180deg, var(--sky-top) 0%, #bcdcf4 55%, var(--sky-bottom) 100%);
  }
  .brand-name {
    position: absolute; left: 0; top: 160px; width: 980px;
    text-align: center;
    font-weight: 700;
    font-size: 74px;
    line-height: 1.1;
    color: var(--brand-green);
  }
  .service-pill {
    position: absolute; left: 54px; top: 441px; width: 871px; height: 112px;
    border-radius: 56px;
    background: var(--pill-orange);
    color: var(--white);
    text-align: center;
  }
  .service-pill .intro {
    position: absolute; left: 0; right: 0; top: 6px;
    font-size: 33px; line-height: 44px;
  }
  .service-pill .headline {
    position: absolute; left: 0; right: 0; top: 50px;
    font-weight: 400;
    font-size: 41px; line-height: 54px; letter-spacing: 3px;
  }
  .lawn-photo {
    position: absolute; left: 0; top: 569px; width: 980px; height: 631px;
    background:
      radial-gradient(ellipse 420px 180px at 620px 90px, rgba(40,90,30,0.85), transparent 70%),
      radial-gradient(ellipse 260px 300px at 90px 220px, rgba(30,50,90,0.55), transparent 70%),
      linear-gradient(180deg, var(--lawn-dark) 0%, var(--lawn-mid) 30%, var(--lawn-light) 60%, var(--lawn-mid) 100%);
  }
  .certified-badge {
    position: absolute; left: 500px; top: 687px; width: 480px; height: 183px;
    background: var(--badge-blue);
    border-top-left-radius: 42px;
    color: var(--white);
    text-align: right;
    padding: 20px 40px 0 0;
    font-style: italic;
    font-size: 38px;
    line-height: 50px;
    letter-spacing: 0.5px;
    white-space: nowrap;
  }
  .contact-bar {
    position: absolute; left: 0; top: 1001px; width: 980px; height: 141px;
    background: var(--white);
  }
  .contact-bar .accent {
    position: absolute; left: 0; top: 0; width: 158px; height: 141px;
    background: linear-gradient(90deg, var(--bar-orange) 0 48%, var(--bar-orange-deep) 50%, var(--bar-orange) 100%);
  }
  .contact-bar .mail-icon { position: absolute; left: 190px; top: 20px; }
  .contact-bar .email {
    position: absolute; left: 275px; top: 12px;
    font-size: 36px; line-height: 52px; letter-spacing: 0.5px; color: var(--ink);
    white-space: nowrap;
  }
  .contact-bar .phone {
    position: absolute; left: 190px; top: 68px;
    font-size: 40px; line-height: 66px; color: var(--ink);
    white-space: nowrap;
  }
  .contact-bar .phone .number {
    font-size: 56px; letter-spacing: 6px; margin-left: 10px;
  }
</style>
</head>
<body>
<main class="ad">
  <section class="sky" aria-hidden="true"></section>
  <h1 class="brand-name">Halvern Lawn Works</h1>

  <section class="service-pill">
    <p class="intro">We offer single applications or season long</p>
    <h2 class="headline">Fertilizer &amp; Weed control programs</h2>
  </section>

  <div class="lawn-photo" role="img" aria-label="Photo of a lawn technician working on a bright green lawn with a flowering hedge behind"></div>

  <p class="certified-badge">All of our technicians<br>are certified by<br>Prairie Environment</p>

  <section class="contact-bar">
    <div class="accent" aria-hidden="true"></div>
    <svg class="mail-icon" width="60" height="40" viewBox="0 0 60 40" aria-hidden="true">
      <rect x="1" y="1" width="58" height="38" rx="6" fill="#1d1d1d"/>
      <path d="M6 6 L30 24 L54 6 M6 34 L23 19 M54 34 L37 19" stroke="#fff" stroke-width="3" fill="none"/>
    </svg>
    <p class="email">halvernlawnworks@mailpost.test</p>
    <p class="phone">Call or Text: <span class="number">555-814-2937</span></p>
  </section>
</main>
</body>
</html>
```